Business Card Design Project

Basic business card with minimal details. I just need company name, email & web address, telephone and my name.
I would like the back of the card to be grey with my logo & company name centred.

Target Market(s)

Architects
Builders
Property Developers

Industry/Entity Type

Business

Font styles to use
Sans Serif

Colors

Designer to choose colors to be used in the design.

Requirements
Must have
• Framewise Build
Marcus Helby - Director
M: 0427 593184
E: marcus@framewisebuild.com.au
W: www.framewisebuild.com.au
Should not have
• No other images or pictures

```html
<!DOCTYPE html>
<html lang="en">
<head>
<meta charset="utf-8">
<title>Framewise Build — Business Card</title>
<link rel="stylesheet" href="https://fonts.googleapis.com/css2?family=Roboto:wght@400;500&display=swap">
<style>
  :root {
    --page: #e9e7e4;
    --card-grey: #b9bbbc;
    --card-light: #eeeeee;
    --brand-blue: #1f93d8;
    --ink: #4b5560;
    --text-light: #ffffff;
    --icon-ring: #1f93d8;
  }
  * { box-sizing: border-box; margin: 0; padding: 0; }
  html, body { width: 1200px; height: 900px; overflow: hidden; }
  body {
    background: var(--page);
    font-family: "Roboto", Arial, sans-serif;
    display: flex;
    flex-direction: column;
    align-items: center;
    justify-content: center;
    gap: 56px;
  }
  .card {
    position: relative;
    width: 620px;
    height: 378px;
    background: radial-gradient(circle at 50% 45%, var(--card-light) 0%, var(--card-grey) 62%);
    box-shadow: 0 6px 18px rgba(0,0,0,0.18);
    overflow: hidden;
  }

  /* Front */
  .front-brand {
    position: absolute;
    left: 70px;
    top: 118px;
    display: flex;
    align-items: center;
    gap: 12px;
  }
  .brand-square {
    width: 26px; height: 26px;
    background: #b0243a;
  }
  .brand-name {
    font-weight: 500;
    font-size: 26px;
    letter-spacing: 2px;
    text-transform: uppercase;
    color: var(--ink);
  }
  .name-band {
    position: absolute;
    left: 320px;
    top: 170px;
    width: 300px;
    height: 58px;
    background: var(--brand-blue);
    clip-path: polygon(18px 0, 100% 0, 100% 100%, 0 100%);
    color: var(--text-light);
    padding: 8px 0 0 40px;
  }
  .person-name { font-size: 20px; font-weight: 500; line-height: 1.1; }
  .person-role { font-size: 13px; line-height: 1.4; }
  .contact-list {
    position: absolute;
    left: 250px;
    top: 244px;
    list-style: none;
  }
  .contact-item {
    display: flex;
    align-items: center;
    height: 32px;
    font-size: 14px;
    color: var(--text-light);
  }
  .contact-lead {
    width: 60px; height: 4px;
    background: var(--brand-blue);
  }
  .contact-icon { width: 24px; height: 24px; margin-right: 14px; }

  /* Back */
  .back-frame {
    position: absolute;
    inset: 34px 40px;
    border: 2px solid var(--brand-blue);
  }
  .back-brand {
    position: absolute;
    inset: 0;
    display: flex;
    flex-direction: column;
    align-items: center;
    justify-content: center;
    gap: 18px;
  }
  .back-brand .brand-square { width: 44px; height: 44px; }
  .back-brand .brand-name { font-size: 32px; }
</style>
</head>
<body>

<section class="card card-front" aria-label="Business card front">
  <div class="front-brand">
    <span class="brand-square"></span>
    <span class="brand-name">Framewise Build</span>
  </div>

  <div class="name-band">
    <div class="person-name">Marcus Helby</div>
    <div class="person-role">Director</div>
  </div>

  <ul class="contact-list">
    <li class="contact-item">
      <span class="contact-lead"></span>
      <svg class="contact-icon" viewBox="0 0 24 24" aria-hidden="true">
        <circle cx="12" cy="12" r="10.5" fill="#fff" stroke="var(--icon-ring)" stroke-width="2.5"/>
        <path d="M9 7.5l2 2-1.2 1.3c.6 1.4 1.6 2.4 3 3L14 12.6l2 2-1.3 1.6c-3.4-.4-6.5-3.5-6.9-6.9z" fill="#8b949c"/>
      </svg>
      0427 593184
    </li>
    <li class="contact-item">
      <span class="contact-lead"></span>
      <svg class="contact-icon" viewBox="0 0 24 24" aria-hidden="true">
        <circle cx="12" cy="12" r="10.5" fill="#fff" stroke="var(--icon-ring)" stroke-width="2.5"/>
        <rect x="7" y="8.5" width="10" height="7" fill="#8b949c"/>
        <path d="M7 8.5l5 4 5-4" fill="none" stroke="#fff" stroke-width="1"/>
      </svg>
      marcus@framewisebuild.com.au
    </li>
    <li class="contact-item">
      <span class="contact-lead"></span>
      <svg class="contact-icon" viewBox="0 0 24 24" aria-hidden="true">
        <circle cx="12" cy="12" r="10.5" fill="#fff" stroke="var(--icon-ring)" stroke-width="2.5"/>
        <circle cx="12" cy="12" r="5" fill="none" stroke="#8b949c" stroke-width="1.4"/>
        <path d="M7 12h10M12 7c-2 2.8-2 7.2 0 10M12 7c2 2.8 2 7.2 0 10" fill="none" stroke="#8b949c" stroke-width="1"/>
      </svg>
      www.framewisebuild.com.au
    </li>
  </ul>
</section>

<section class="card card-back" aria-label="Business card back">
  <div class="back-frame"></div>
  <div class="back-brand">
    <span class="brand-square"></span>
    <span class="brand-name">Framewise Build</span>
  </div>
</section>

</body>
</html>
```